LKT business card design

Coastal Guard Auxiliary Kin Services exists to provide timely and relevant programs and services to assist commanders with their role to ensure their assigned Families (Soldiers, spouses, children, significant others) have the highest possible level of well-being, and are the "ready" (for deployment, family separation, and self-sufficiency during that separation). We accomplish this task through several functional areas: Leadership (Director), Coordination (Coordinator--coordinates a variety of human services, staff sections, sister agencies, etc. to offer training and support), unit Family Readiness Programs, Junior Learner and Campus Aid, Bereaved Contact Network, Lantern Path Initiative (deployment and reintegration training), Recovery Care (for wounded warriors), Crisis Intervention, and Prevention Education and Training. Our aim is to demonstrate "Kin Above All" in everything we do, because Family Readiness improves Soldier Readiness which improves Army Readiness.

Folks, I've tried to upload the logos I mentioned, with not luck. You can get a look at one version of the Guard Auxiliary Kin Services logo at www.gaks-example.org.

Reason: Extendinig a couple days because I've not yet had any sucess uploading logos I mention in the brief. Hoping to crack the nut on that soon Thanks for your patient work.

Target Market(s)

Army Reserve Commanders, First Sergeants, Adult & Youth Volunteers & Family Members who are called to contribute to Whole Guard Kin readiness by being skilled at handling the challendes of deployment, family separation, and the self-sufficiency required when their Soldier deploys (e.g., fulfilling the Soldiers roles on the homefront while he or she is away)

Industry/Entity Type

Training

Contact Information for Business Card

Dr. Marcus T. Holloway, Director
Family Programs, 4th RDG, CGAWEST
2846 Ridge Lane
Honolulu, HI 96502-4718
808-555-0172 ext. 4820
BB: 808-555-0639
marcus.t.holloway7.staff@postbox-example.net

Requirements
Must have
• Family Programs Logo with text
Nice to have
• 4th RDG and CGAWEST Logo
Should not have
• old GAKS Logo (Green, blue globe with family silhouette)

```html
<!DOCTYPE html>
<html lang="en">
<head>
<meta charset="utf-8">
<title>LKT Business Card – Dr. Marcus T. Holloway</title>
<link rel="stylesheet" href="https://fonts.googleapis.com/css2?family=Exo+2:wght@400;500&display=swap">
<style>
  :root {
    --card-white: #ffffff;
    --brand-green: #5c9b3e;
    --name-green: #6aab45;
    --ink-white: #ffffff;
    --mark-dark: #2b2b2b;
    --page-bg: #e9e9e9;
  }
  * { margin: 0; padding: 0; box-sizing: border-box; }
  html, body { width: 1200px; height: 614px; overflow: hidden; background: var(--page-bg); }
  .card {
    position: relative;
    width: 1200px; height: 614px;
    background: var(--card-white);
    font-family: "Exo 2", "Open Sans", sans-serif;
    overflow: hidden;
  }
  .identity {
    position: absolute; top: 0; left: 0; right: 0; height: 286px;
  }
  .org-mark {
    position: absolute; left: 34px; top: 40px;
    width: 200px; height: 150px;
    display: flex; align-items: center; gap: 12px;
    color: var(--brand-green); font-weight: 500; font-size: 22px; line-height: 1.2;
  }
  .org-mark .dot {
    flex: 0 0 28px; height: 28px; border-radius: 50%; background: var(--brand-green);
  }
  .partner-mark {
    position: absolute; left: 1020px; top: 70px;
    width: 150px; height: 168px;
    display: flex; flex-direction: column; align-items: center; justify-content: center; gap: 12px;
    color: var(--mark-dark); font-weight: 500; font-size: 24px; text-align: center; line-height: 1.15;
  }
  .partner-mark .square { width: 46px; height: 46px; background: var(--mark-dark); }
  .holder {
    position: absolute; left: 300px; right: 240px; top: 78px;
    text-align: center; color: var(--name-green);
    font-weight: 400; font-size: 45px; line-height: 62px;
  }
  .contact {
    position: absolute; left: 0; right: 0; top: 286px; bottom: 0;
    background: var(--brand-green); color: var(--ink-white);
    font-size: 33px; font-weight: 400;
  }
  .contact-row { position: absolute; left: 223px; line-height: 42px; white-space: nowrap; }
  .contact-row svg { position: absolute; left: -70px; top: 4px; width: 34px; height: 34px; }
  .row-address { top: 30px; }
  .row-phone { top: 172px; }
  .row-email { top: 250px; }
</style>
</head>
<body>
<main class="card">
  <section class="identity">
    <div class="org-mark"><span class="dot"></span><span>Guard Auxiliary Kin Services</span></div>
    <h1 class="holder">Dr. Marcus T. Holloway<br>Director Family Programs</h1>
    <div class="partner-mark"><span class="square"></span><span>Coastal Guard</span></div>
  </section>
  <section class="contact">
    <div class="contact-row row-address">
      <svg viewBox="0 0 24 24" aria-hidden="true"><path d="M12 2a7 7 0 0 0-7 7c0 5 7 13 7 13s7-8 7-13a7 7 0 0 0-7-7z" fill="none" stroke="currentColor" stroke-width="1.6"/><circle cx="12" cy="9" r="2.4" fill="none" stroke="currentColor" stroke-width="1.6"/></svg>
      4th RDG, CGAWEST<br>2846 Ridge Lane Honolulu, HI&nbsp; - 96502-4718
    </div>
    <div class="contact-row row-phone">
      <svg viewBox="0 0 24 24" aria-hidden="true"><rect x="7" y="2" width="10" height="20" rx="2" fill="none" stroke="currentColor" stroke-width="1.6"/><line x1="10.5" y1="18.5" x2="13.5" y2="18.5" stroke="currentColor" stroke-width="1.6"/></svg>
      808-555-0172&nbsp; ext. 4820&nbsp; BB: 808-555-0639
    </div>
    <div class="contact-row row-email">
      <svg viewBox="0 0 24 24" aria-hidden="true"><rect x="2.5" y="5" width="19" height="14" fill="none" stroke="currentColor" stroke-width="1.6"/><polyline points="2.5,5 12,13 21.5,5" fill="none" stroke="currentColor" stroke-width="1.6"/></svg>
      marcus.t.holloway7.staff@postbox-example.net
    </div>
  </section>
</main>
</body>
</html>
```